Business Card Design

We Need a business card design for my company based in Tv Radio and music Productions and hunt Talent.

Industry/Entity Type

Business

Contact Information for Business Card

BrentaVue Production's, Teodor Vignoles,Cell Phone 318 4957310
Musician, Productor, Hunt Talent. Miami Fla. www.brentavue.net Mail. teodorvignoles@mailvana.com

```html
<!DOCTYPE html>
<html lang="en">
<head>
<meta charset="utf-8">
<title>BrentaVue Production's — Business Card</title>
<link href="https://fonts.googleapis.com/css2?family=PT+Sans:wght@400;700&display=swap" rel="stylesheet">
<style>
  :root{
    --bg:#e9e6e2;
    --card:#ffffff;
    --ink:#1f1a17;
    --gold:#d6b321;
    --amber:#b8752a;
    --crimson:#9b1b1c;
    --mark:#a3211f;
    --band:linear-gradient(90deg,var(--gold) 0%,var(--amber) 45%,var(--crimson) 100%);
  }
  *{box-sizing:border-box;margin:0;padding:0}
  html,body{width:1200px;height:1000px;overflow:hidden}
  body{background:var(--bg);font-family:"PT Sans",sans-serif;color:var(--ink);position:relative}

  .card{position:absolute;width:640px;height:320px;background:var(--card);
        box-shadow:0 6px 18px rgba(0,0,0,.18);overflow:hidden}
  .card--front{left:280px;top:100px}
  .card--back{left:280px;top:560px}

  .rule{position:absolute;left:0;right:0;height:3px;background:var(--band)}
  .band{position:absolute;left:0;right:0;background:var(--band)}

  .brand{position:absolute;display:flex;align-items:center;gap:10px}
  .brand__dot{width:46px;height:46px;border-radius:50%;background:var(--gold)}
  .brand__name{font-weight:700;font-size:30px;color:var(--mark)}

  .company{position:absolute;font-weight:700;font-size:26px;white-space:nowrap}
  .person{position:absolute;font-weight:700;font-size:26px;white-space:nowrap}

  .details{position:absolute;left:34px;font-size:14px;line-height:1.55}
  .details__role{font-weight:700}
  .details__label{font-weight:700}

  /* front */
  .card--front .brand{left:32px;top:48px}
  .card--front .company{left:300px;top:120px}
  .card--front .person{left:32px;top:140px}
  .card--front .rule--a{top:176px}
  .card--front .rule--b{top:184px}
  .card--front .band{top:191px;height:96px}
  .card--front .rule--c{top:292px}
  .card--front .rule--d{top:299px}
  .card--front .details{top:212px}

  /* back */
  .card--back .brand{left:50%;top:50px;transform:translateX(-50%)}
  .card--back .company{left:50%;top:140px;transform:translateX(-50%)}
  .card--back .rule--a{top:128px}
  .card--back .rule--b{top:136px}
  .card--back .band{top:143px;height:138px}
  .card--back .rule--c{top:286px}
  .card--back .rule--d{top:293px}
  .card--back .company{top:172px;color:var(--ink)}
  .card--back .brand{top:52px}
</style>
</head>
<body>
  <section class="card card--front" aria-label="Business card front">
    <div class="brand">
      <span class="brand__dot"></span>
      <span class="brand__name">BrentaVue</span>
    </div>
    <div class="company">BrentaVue Production's</div>
    <div class="person">Teodor Vignoles</div>
    <div class="rule rule--a"></div>
    <div class="rule rule--b"></div>
    <div class="band"></div>
    <div class="rule rule--c"></div>
    <div class="rule rule--d"></div>
    <div class="details">
      <p class="details__role">Musician, Productor, Hunt Talent. Miami Fla</p>
      <p><span class="details__label">t:</span> 318 4957310 - <span class="details__label">e:</span> teodorvignoles@mailvana.com - <span class="details__label">w:</span> www.brentavue.net</p>
    </div>
  </section>

  <section class="card card--back" aria-label="Business card back">
    <div class="brand">
      <span class="brand__dot"></span>
      <span class="brand__name">BrentaVue</span>
    </div>
    <div class="rule rule--a"></div>
    <div class="rule rule--b"></div>
    <div class="band"></div>
    <div class="rule rule--c"></div>
    <div class="rule rule--d"></div>
    <div class="company">BrentaVue Production's</div>
  </section>
</body>
</html>
```